3 out of 100 people will get deadly skin cancer - we need a great illustration that shows this!

We put together a prototype image that communicates lifetime skin cancer risk. (see attached). We are looking for illustrators who can take make a new/better/cooler graphic that communicates this idea. It could be as simple as a superior illustration of the graphic we have or illustrators can propose a completely different idea.What should the illustration communicate?U.S. adults have a lifetime risk of developing skin cancer of 1 in 5. But we don't want to show 1 in 5; we want to show that number in a larger group. For example, in the attached illustration we show 20 in 100 people get skin cancer (i.e., 100 beach towels/umbrellas and 20 of them are red). Research has shown that people are more likely to accurately understand numbers like this when you convey them for larger groups (i.e., 20 out of 100 rather than 1 out of 5). U.S. adults also have a lifetime risk of 2.3% of developing the deadliest form of skin cancer (melanoma). In other words, approximately 3 in 100 people will develop melanoma in their lifetime. Ideally, a single image will convey both lifetime skin cancer risk (20 in 100) and melanoma risk (3 in 100). We will award a top three as follows: 1st place = $300, 2nd place = $250, third place = $200. We will also buy any design beyond 3rd place that we like for $100. For example, we purchased 24 designs in our last contest on Artquilla.This research is supported by funding from the University of Brenmoor.

Target Market(s)

The U.S. public; individuals at high risk of developing skin cancer

Industry/Entity Type

Medicine

Colors

Designer to choose colors to be used in the design.

Requirements
Must have
• an original illustration that conveys both lifetime risk of developing skin cancer (20 in 100) and melanoma (3 in 100).
Nice to have
• It can be beach towels and umbrellas, just like our prototype, or the designers can pitch an original idea. Imagery can be realistic or cartoonish (or something in between). It should be illustrations, though. Not edited photos. The image should be in color (no black and white illustrations).
Should not have
• Photos. Clip art. Free vector images.
• We are looking for original illustrations created by the designer.

```html
<!DOCTYPE html>
<html lang="en">
<head>
<meta charset="utf-8">
<title>Lifetime Skin Cancer Risk – Ocean School</title>
<link href="https://fonts.googleapis.com/css2?family=Open+Sans:wght@700&display=swap" rel="stylesheet">
<style>
  :root {
    --page: #ffffff;
    --legend-band: #e3e3e3;
    --water-edge: #7ef8fd;
    --water-glow: #d2fcf6;
    --fish-healthy: #0a0ae6;
    --fish-cancer: #f5146e;
    --fish-melanoma: #000000;
    --ink: #111111;
    --weed-light: #8ee60a;
    --weed-deep: #22b40f;
    --seabed: #0d5a06;
    --star-gold: #efb917;
    --star-orange: #ec6a0b;
  }
  * { box-sizing: border-box; margin: 0; padding: 0; }
  html, body {
    width: 1200px; height: 1200px; overflow: hidden;
    background: var(--page);
  }
  .canvas { position: relative; width: 1200px; height: 1200px; }

  .legend {
    position: absolute; left: 76px; top: 218px;
    width: 1057px; height: 106px;
    background: var(--legend-band);
  }
  .legend-item {
    position: absolute; top: 38px;
    display: flex; align-items: center; gap: 30px;
    font-family: "Open Sans", Arial, sans-serif;
    font-weight: 700; font-size: 25px; color: var(--ink);
    white-space: nowrap;
  }
  .legend-item--healthy { left: 70px; }
  .legend-item--cancer { left: 406px; }
  .legend-item--melanoma { left: 714px; }
  .legend-swatch {
    width: 50px; height: 22px; border-radius: 11px;
    transform: rotate(35deg);
  }
  .legend-swatch--healthy { background: var(--fish-healthy); }
  .legend-swatch--cancer { background: var(--fish-cancer); }
  .legend-swatch--melanoma { background: linear-gradient(90deg, var(--fish-cancer) 65%, var(--fish-melanoma) 65%); }

  .ocean {
    position: absolute; left: 76px; top: 324px;
    width: 1057px; height: 541px;
    background: radial-gradient(ellipse at 50% 60%, var(--water-glow) 0%, var(--water-edge) 70%);
  }

  .risk-chart { position: absolute; left: 0; top: 0; width: 1200px; height: 1200px; }
  .fish--healthy { fill: var(--fish-healthy); }
  .fish--cancer { fill: var(--fish-cancer); }
  .melanoma-stop-a { stop-color: var(--fish-cancer); }
  .melanoma-stop-b { stop-color: var(--fish-melanoma); }

  .seaweed {
    position: absolute; left: 76px; top: 704px;
    width: 1057px; height: 161px;
    background: linear-gradient(180deg, var(--weed-light) 0%, var(--weed-deep) 70%, var(--seabed) 100%);
    border-radius: 40px 40px 0 0;
  }

  .starfish {
    position: absolute; width: 120px; height: 110px; border-radius: 50%;
  }
  .starfish--left { left: 56px; top: 302px; background: var(--star-gold); }
  .starfish--right { left: 1024px; top: 280px; background: var(--star-orange); }
</style>
</head>
<body>
<main class="canvas">
  <section class="legend">
    <div class="legend-item legend-item--healthy">
      <span class="legend-swatch legend-swatch--healthy"></span>
      <span>No Skin Cancer</span>
    </div>
    <div class="legend-item legend-item--cancer">
      <span class="legend-swatch legend-swatch--cancer"></span>
      <span>Skin Cancer</span>
    </div>
    <div class="legend-item legend-item--melanoma">
      <span class="legend-swatch legend-swatch--melanoma"></span>
      <span>Melanoma</span>
    </div>
  </section>

  <section class="ocean" role="img" aria-label="Light turquoise underwater scene"></section>

  <svg class="risk-chart" viewBox="0 0 1200 1200" role="img" aria-label="100 markers in two fan-shaped schools: 80 blue, 20 pink for skin cancer, 3 of them with black heads for melanoma">
    <defs>
      <linearGradient id="melanoma-fill" x1="0" y1="0" x2="1" y2="0">
        <stop offset="0.62" class="melanoma-stop-a"/>
        <stop offset="0.62" class="melanoma-stop-b"/>
      </linearGradient>
      <rect id="fish-h" class="fish--healthy" x="-207" y="-10" width="58" height="20" rx="10"/>
      <rect id="fish-c" class="fish--cancer" x="-207" y="-10" width="58" height="20" rx="10"/>
      <rect id="fish-m" fill="url(#melanoma-fill)" x="-207" y="-10" width="58" height="20" rx="10"/>
    </defs>

    <g class="school school--left">
      <!-- column 1 -->
      <use href="#fish-h" transform="translate(342 544) rotate(52)"/>
      <use href="#fish-m" transform="translate(342 544) rotate(40.4)"/>
      <use href="#fish-h" transform="translate(342 544) rotate(28.9)"/>
      <use href="#fish-h" transform="translate(342 544) rotate(17.3)"/>
      <use href="#fish-h" transform="translate(342 544) rotate(5.8)"/>
      <use href="#fish-h" transform="translate(342 544) rotate(-5.8)"/>
      <use href="#fish-h" transform="translate(342 544) rotate(-17.3)"/>
      <use href="#fish-h" transform="translate(342 544) rotate(-28.9)"/>
      <use href="#fish-h" transform="translate(342 544) rotate(-40.4)"/>
      <use href="#fish-c" transform="translate(342 544) rotate(-52)"/>
      <!-- column 2 -->
      <use href="#fish-h" transform="translate(422 544) rotate(52)"/>
      <use href="#fish-h" transform="translate(422 544) rotate(40.4)"/>
      <use href="#fish-h" transform="translate(422 544) rotate(28.9)"/>
      <use href="#fish-h" transform="translate(422 544) rotate(17.3)"/>
      <use href="#fish-c" transform="translate(422 544) rotate(5.8)"/>
      <use href="#fish-h" transform="translate(422 544) rotate(-5.8)"/>
      <use href="#fish-c" transform="translate(422 544) rotate(-17.3)"/>
      <use href="#fish-h" transform="translate(422 544) rotate(-28.9)"/>
      <use href="#fish-h" transform="translate(422 544) rotate(-40.4)"/>
      <use href="#fish-h" transform="translate(422 544) rotate(-52)"/>
      <!-- column 3 -->
      <use href="#fish-c" transform="translate(506 544) rotate(52)"/>
      <use href="#fish-h" transform="translate(506 544) rotate(40.4)"/>
      <use href="#fish-h" transform="translate(506 544) rotate(28.9)"/>
      <use href="#fish-h" transform="translate(506 544) rotate(17.3)"/>
      <use href="#fish-h" transform="translate(506 544) rotate(5.8)"/>
      <use href="#fish-h" transform="translate(506 544) rotate(-5.8)"/>
      <use href="#fish-h" transform="translate(506 544) rotate(-17.3)"/>
      <use href="#fish-h" transform="translate(506 544) rotate(-28.9)"/>
      <use href="#fish-c" transform="translate(506 544) rotate(-40.4)"/>
      <use href="#fish-h" transform="translate(506 544) rotate(-52)"/>
      <!-- column 4 -->
      <use href="#fish-h" transform="translate(590 544) rotate(52)"/>
      <use href="#fish-h" transform="translate(590 544) rotate(40.4)"/>
      <use href="#fish-h" transform="translate(590 544) rotate(28.9)"/>
      <use href="#fish-h" transform="translate(590 544) rotate(17.3)"/>
      <use href="#fish-m" transform="translate(590 544) rotate(5.8)"/>
      <use href="#fish-h" transform="translate(590 544) rotate(-5.8)"/>
      <use href="#fish-h" transform="translate(590 544) rotate(-17.3)"/>
      <use href="#fish-h" transform="translate(590 544) rotate(-28.9)"/>
      <use href="#fish-c" transform="translate(590 544) rotate(-40.4)"/>
      <use href="#fish-h" transform="translate(590 544) rotate(-52)"/>
      <!-- column 5 -->
      <use href="#fish-h" transform="translate(674 544) rotate(52)"/>
      <use href="#fish-h" transform="translate(674 544) rotate(40.4)"/>
      <use href="#fish-h" transform="translate(674 544) rotate(28.9)"/>
      <use href="#fish-c" transform="translate(674 544) rotate(17.3)"/>
      <use href="#fish-h" transform="translate(674 544) rotate(5.8)"/>
      <use href="#fish-h" transform="translate(674 544) rotate(-5.8)"/>
      <use href="#fish-h" transform="translate(674 544) rotate(-17.3)"/>
      <use href="#fish-h" transform="translate(674 544) rotate(-28.9)"/>
      <use href="#fish-h" transform="translate(674 544) rotate(-40.4)"/>
      <use href="#fish-c" transform="translate(674 544) rotate(-52)"/>
    </g>

    <g class="school school--right" transform="translate(1200 0) scale(-1 1)">
      <!-- column 1 (outermost) -->
      <use href="#fish-h" transform="translate(338 544) rotate(52)"/>
      <use href="#fish-h" transform="translate(338 544) rotate(40.4)"/>
      <use href="#fish-c" transform="translate(338 544) rotate(28.9)"/>
      <use href="#fish-h" transform="translate(338 544) rotate(17.3)"/>
      <use href="#fish-h" transform="translate(338 544) rotate(5.8)"/>
      <use href="#fish-h" transform="translate(338 544) rotate(-5.8)"/>
      <use href="#fish-h" transform="translate(338 544) rotate(-17.3)"/>
      <use href="#fish-h" transform="translate(338 544) rotate(-28.9)"/>
      <use href="#fish-c" transform="translate(338 544) rotate(-40.4)"/>
      <use href="#fish-h" transform="translate(338 544) rotate(-52)"/>
      <!-- column 2 -->
      <use href="#fish-h" transform="translate(418 544) rotate(52)"/>
      <use href="#fish-c" transform="translate(418 544) rotate(40.4)"/>
      <use href="#fish-h" transform="translate(418 544) rotate(28.9)"/>
      <use href="#fish-h" transform="translate(418 544) rotate(17.3)"/>
      <use href="#fish-c" transform="translate(418 544) rotate(5.8)"/>
      <use href="#fish-h" transform="translate(418 544) rotate(-5.8)"/>
      <use href="#fish-c" transform="translate(418 544) rotate(-17.3)"/>
      <use href="#fish-h" transform="translate(418 544) rotate(-28.9)"/>
      <use href="#fish-h" transform="translate(418 544) rotate(-40.4)"/>
      <use href="#fish-h" transform="translate(418 544) rotate(-52)"/>
      <!-- column 3 -->
      <use href="#fish-h" transform="translate(498 544) rotate(52)"/>
      <use href="#fish-c" transform="translate(498 544) rotate(40.4)"/>
      <use href="#fish-h" transform="translate(498 544) rotate(28.9)"/>
      <use href="#fish-h" transform="translate(498 544) rotate(17.3)"/>
      <use href="#fish-h" transform="translate(498 544) rotate(5.8)"/>
      <use href="#fish-h" transform="translate(498 544) rotate(-5.8)"/>
      <use href="#fish-h" transform="translate(498 544) rotate(-17.3)"/>
      <use href="#fish-h" transform="translate(498 544) rotate(-28.9)"/>
      <use href="#fish-m" transform="translate(498 544) rotate(-40.4)"/>
      <use href="#fish-h" transform="translate(498 544) rotate(-52)"/>
      <!-- column 4 -->
      <use href="#fish-h" transform="translate(582 544) rotate(52)"/>
      <use href="#fish-c" transform="translate(582 544) rotate(40.4)"/>
      <use href="#fish-h" transform="translate(582 544) rotate(28.9)"/>
      <use href="#fish-h" transform="translate(582 544) rotate(17.3)"/>
      <use href="#fish-h" transform="translate(582 544) rotate(5.8)"/>
      <use href="#fish-h" transform="translate(582 544) rotate(-5.8)"/>
      <use href="#fish-c" transform="translate(582 544) rotate(-17.3)"/>
      <use href="#fish-h" transform="translate(582 544) rotate(-28.9)"/>
      <use href="#fish-h" transform="translate(582 544) rotate(-40.4)"/>
      <use href="#fish-h" transform="translate(582 544) rotate(-52)"/>
      <!-- column 5 (innermost) -->
      <use href="#fish-h" transform="translate(666 544) rotate(52)"/>
      <use href="#fish-h" transform="translate(666 544) rotate(40.4)"/>
      <use href="#fish-h" transform="translate(666 544) rotate(28.9)"/>
      <use href="#fish-h" transform="translate(666 544) rotate(17.3)"/>
      <use href="#fish-h" transform="translate(666 544) rotate(5.8)"/>
      <use href="#fish-h" transform="translate(666 544) rotate(-5.8)"/>
      <use href="#fish-h" transform="translate(666 544) rotate(-17.3)"/>
      <use href="#fish-h" transform="translate(666 544) rotate(-28.9)"/>
      <use href="#fish-c" transform="translate(666 544) rotate(-40.4)"/>
      <use href="#fish-h" transform="translate(666 544) rotate(-52)"/>
    </g>
  </svg>

  <div class="seaweed" role="img" aria-label="Green seaweed rising from a dark green seabed"></div>

  <div class="starfish starfish--left" role="img" aria-label="Yellow starfish"></div>
  <div class="starfish starfish--right" role="img" aria-label="Orange starfish"></div>
</main>
</body>
</html>
```